MGA - Meridale Growth Advisory

We need a website designed for a new company based in the UAE. MGA is a business consultancy training company aiming to provide strategic and sustainable solutions for their people and offer human development. The company offers research based consultancy.

Target Market(s)

Companies

Industry/Entity Type

Business Consultant

Number of Pages Required

2 page

Font styles to use
Other font styles liked:
• Century Gothic

Requirements
Must have
• Please look at other consultancy companies and make sure we have the main things on it.

```html
<!DOCTYPE html>
<html lang="en">
<head>
<meta charset="utf-8">
<title>MGA - Meridale Growth Advisory</title>
<link href="https://fonts.googleapis.com/css2?family=Open+Sans:wght@300;400;600;700&display=swap" rel="stylesheet">
<style>
:root{
  --teal:#1fa396;
  --ink:#2b2b2b;
  --text:#6f6f6f;
  --muted:#9a9a9a;
  --line:#e6e6e6;
  --footer:#2e2e2e;
  --footer-base:#262626;
  --footer-text:#9b9b9b;
  --white:#ffffff;
}
*{box-sizing:border-box;margin:0;padding:0}
html,body{width:1200px;height:2200px;overflow:hidden}
body{font-family:"Open Sans",Arial,sans-serif;color:var(--ink);background:var(--white);position:relative}
.wrap{width:1001px;margin:0 auto;position:relative}

/* header */
.site-header{height:84px;border-top:1px solid var(--line);border-bottom:1px solid var(--line)}
.site-header .wrap{display:flex;align-items:center;height:100%;justify-content:space-between}
.brand{display:flex;align-items:center;gap:10px;font-size:15px;line-height:17px;color:var(--ink);width:150px}
.brand-mark{width:26px;height:26px;border-radius:50%;background:var(--ink);flex:none}
.main-nav{display:flex;gap:0}
.main-nav a{font-size:13px;color:var(--ink);text-decoration:none;margin-left:78px;display:flex;align-items:center;gap:6px}
.main-nav a:first-child{margin-left:0}

/* hero */
.hero{height:481px;position:relative;overflow:hidden;text-align:center;color:var(--white)}
.hero-photo{position:absolute;inset:0;background:linear-gradient(100deg,#3e4f4d 0%,#5b6c69 30%,#8a9896 55%,#b7c2c0 80%,#9ea9a7 100%)}
.hero-shade{position:absolute;inset:0;background:rgba(20,40,38,.45)}
.hero-content{position:relative;padding-top:190px}
.hero-name{font-size:60px;font-weight:600;letter-spacing:2px;margin-bottom:28px}
.hero-title{font-size:33px;font-weight:700;letter-spacing:1px;display:flex;justify-content:center;align-items:center;gap:14px}
.hero-title i{width:9px;height:9px;border-radius:50%;background:var(--teal);display:inline-block}
.hero-sub{font-size:15px;font-weight:300;letter-spacing:1px;margin-top:12px;text-transform:uppercase}
.hero-arrow{position:absolute;top:320px;width:26px;height:26px;border-radius:50%;background:rgba(255,255,255,.12)}
.hero-arrow.prev{left:33px}.hero-arrow.next{right:33px}

/* welcome */
.welcome{text-align:center;padding-top:60px}
.welcome h1{font-size:28px;font-weight:400;color:var(--ink)}
.welcome p{font-size:12px;line-height:26px;color:var(--text);width:800px;margin:18px auto 0}
.services{display:flex;gap:1px;margin-top:50px;text-align:left}
.service{width:250px}
.service-photo{height:156px;background:linear-gradient(135deg,#cfcfcf,#6a6a6a)}
.service.active .service-photo{background:linear-gradient(135deg,#2aae9f,#188d82);display:flex;align-items:center;justify-content:center}
.service-photo .ring{width:40px;height:40px;border-radius:50%;background:rgba(255,255,255,.25);display:flex;align-items:center;justify-content:center}
.service h3{font-size:17px;font-weight:400;margin:16px 0 8px}
.service p{font-size:11px;line-height:23px;color:var(--text);width:225px}

/* testimonial */
.testimonial{margin-top:56px;height:280px;position:relative;text-align:center;color:var(--white);overflow:hidden}
.testimonial-photo{position:absolute;inset:0;background:linear-gradient(90deg,#1b3533,#2b4845 40%,#334f4c 70%,#1e3835)}
.testimonial-inner{position:relative;padding-top:56px}
.testimonial blockquote{font-size:13px;line-height:29px;width:860px;margin:22px auto 0}
.testimonial cite{display:block;font-style:normal;font-size:13px;margin-top:18px}
.testimonial cite b{font-weight:700}

/* what we do */
.what{padding-top:76px;height:355px;border-bottom:1px solid var(--line)}
.what .wrap{display:flex;gap:51px}
.what-photo{width:364px;height:206px;background:linear-gradient(120deg,#f1f3f6,#b9c3cc 60%,#5e6b78)}
.what-body{width:560px}
.what h2{font-size:28px;font-weight:400;margin-top:-10px}
.what h4{font-size:13px;font-weight:600;margin-top:14px}
.what p{font-size:11px;line-height:24px;color:var(--text);margin-top:10px}
.btn{display:inline-block;margin-top:20px;background:var(--teal);color:var(--white);font-size:12px;padding:0 30px;height:45px;line-height:45px;border-radius:2px;text-decoration:none}

/* partners */
.partners{height:117px;display:flex;align-items:center}
.partners .wrap{display:flex;justify-content:space-between;align-items:center;padding:0 18px}
.partner{height:34px;width:90px;background:#d7d7d7;border-radius:4px}
.partner.round{width:50px;height:40px;border-radius:50%}

/* footer */
.site-footer{background:var(--footer);height:269px;color:var(--footer-text)}
.site-footer .wrap{display:flex;padding-top:40px}
.footer-brand{width:268px;padding-top:47px;display:flex;align-items:center;gap:12px;font-size:21px;line-height:25px;color:#8c8c8c;font-weight:300}
.footer-brand .brand-mark{background:#8c8c8c;width:40px;height:40px}
.footer-col h5{color:var(--white);font-size:14px;font-weight:600;margin-bottom:20px}
.footer-about{width:398px}
.footer-about p{font-size:11px;line-height:24px;width:330px}
.footer-about a{display:inline-flex;align-items:center;gap:8px;color:var(--white);font-size:11px;margin-top:14px;text-decoration:none}
.footer-links{width:189px}
.footer-links a{display:block;font-size:11px;color:var(--footer-text);text-decoration:none;line-height:27px}
.footer-contact p{font-size:11px;line-height:24px;display:flex;align-items:center;gap:10px}
.footer-base{background:var(--footer-base);height:61px;color:var(--footer-text);font-size:11px}
.footer-base .wrap{display:flex;justify-content:space-between;align-items:center;height:100%}
.social{display:flex;align-items:center;gap:22px}
.social i{width:9px;height:9px;border-radius:50%;background:#8a8a8a;display:inline-block}
</style>
</head>
<body>

<header class="site-header">
  <div class="wrap">
    <a class="brand"><span class="brand-mark"></span><span>Meridale Growth Advisory</span></a>
    <nav class="main-nav">
      <a>Home</a>
      <a>About us</a>
      <a>Services <svg width="7" height="5" viewBox="0 0 7 5"><path d="M0.5 0.8 3.5 3.8 6.5 0.8" fill="none" stroke="#555" stroke-width="1"/></svg></a>
      <a>Testimonials</a>
      <a>Contact us</a>
    </nav>
  </div>
</header>

<section class="hero">
  <div class="hero-photo" role="img" aria-label="Photo of two business people in an office looking ahead"></div>
  <div class="hero-shade"></div>
  <span class="hero-arrow prev"></span><span class="hero-arrow next"></span>
  <div class="hero-content">
    <div class="hero-name">MGA</div>
    <h2 class="hero-title">MERIDALE <i></i> GROWTH <i></i> ADVISORY</h2>
    <p class="hero-sub">We are UAE based. MGA is a business consultancy training company</p>
  </div>
</section>

<section class="welcome">
  <div class="wrap">
    <h1>Welcome to Meridale Growth Advisory</h1>
    <p>We are UAE based. MGA is a business consultancy training company aiming to provide strategic and sustainable solutions for their people and offer human development. The company offers research based consultancy.</p>
    <div class="services">
      <article class="service active">
        <div class="service-photo" role="img" aria-label="Photo of a training session around a meeting table"><span class="ring"><svg width="16" height="16" viewBox="0 0 16 16"><path d="M9 2h5v5M14 2 7 9M12 10v4H2V4h4" fill="none" stroke="#fff" stroke-width="1.6"/></svg></span></div>
        <h3>Training</h3>
        <p>We are UAE based. MGA is a business consultancy training company aiming to provide strategic and sustainable solu-tions for their people...</p>
      </article>
      <article class="service">
        <div class="service-photo" role="img" aria-label="Photo of two consultants working at a laptop"></div>
        <h3>Consulting</h3>
        <p>We are UAE based. MGA is a business consultancy training company aiming to provide strategic and sustainable solu-tions for their people...</p>
      </article>
      <article class="service">
        <div class="service-photo" role="img" aria-label="Photo of a woman holding a light bulb and an ideas folder"></div>
        <h3>Solution</h3>
        <p>We are UAE based. MGA is a business consultancy training company aiming to provide strategic and sustainable solu-tions for their people...</p>
      </article>
      <article class="service">
        <div class="service-photo" role="img" aria-label="Photo of a man looking through binoculars"></div>
        <h3>Research</h3>
        <p>We are UAE based. MGA is a business consultancy training company aiming to provide strategic and sustainable solu-tions for their people...</p>
      </article>
    </div>
  </div>
</section>

<section class="testimonial">
  <div class="testimonial-photo" role="img" aria-label="Darkened photo of colleagues in a meeting"></div>
  <div class="testimonial-inner">
    <svg width="30" height="24" viewBox="0 0 30 24"><path d="M2 24V13C2 6 5 2 12 0v5c-3 1-4 3-4 7h4v12zM18 24V13c0-7 3-11 10-13v5c-3 1-4 3-4 7h4v12z" fill="#fff"/></svg>
    <blockquote>Lorem Ipsum is simply dummy text of the printing and typesetting industry. Lorem Ipsum has been the industry's standard dummy text ever since the 1500s, when an unknown printer took a galley of type and scrambled it to make a type specimen book</blockquote>
    <cite><b>- Leon Haverd -</b> Business man</cite>
  </div>
</section>

<section class="what">
  <div class="wrap">
    <div class="what-photo" role="img" aria-label="Photo of two businessmen reviewing a computer screen"></div>
    <div class="what-body">
      <h2>What we do?</h2>
      <h4>Lorem Ipsum is simply dummy text of the printing and typesetting</h4>
      <p>Lorem Ipsum is simply dummy text of the printing and typesetting industry. Lorem Ipsum has been the industry's standard dummy text ever since the 1500s, when an unknown printer took a galley of type and scrambled it to make a type specimen book industry's standard dummy...</p>
      <a class="btn">Read More Info</a>
    </div>
  </div>
</section>

<section class="partners">
  <div class="wrap">
    <span class="partner round"></span>
    <span class="partner"></span>
    <span class="partner"></span>
    <span class="partner"></span>
    <span class="partner"></span>
    <span class="partner round"></span>
    <span class="partner"></span>
  </div>
</section>

<footer class="site-footer">
  <div class="wrap">
    <div class="footer-brand"><span class="brand-mark"></span><span>Meridale<br>Growth<br>Advisory</span></div>
    <div class="footer-col footer-about">
      <h5>WHO WE ARE?</h5>
      <p>Lorem Ipsum is simply dummy text of the printing and typeset-ting industry. Lorem Ipsum has been the industry's standard dummy text ever since the 1500s, when an unknown printer took a galley of type and scrambled...</p>
      <a>Read more info <svg width="10" height="10" viewBox="0 0 10 10"><circle cx="5" cy="5" r="5" fill="#fff"/><path d="M4 3 6 5 4 7" stroke="#2e2e2e" stroke-width="1.3" fill="none"/></svg></a>
    </div>
    <div class="footer-col footer-links">
      <h5>WELCOME</h5>
      <a>Home</a><a>About us</a><a>Services</a><a>Testimonials</a><a>Contact us</a>
    </div>
    <div class="footer-col footer-contact">
      <h5>CONTACT INFO</h5>
      <p>120 Street name, City name,<br>Country name : 3652235</p>
      <p style="margin-top:6px"><svg width="11" height="9" viewBox="0 0 11 9"><rect x="0" y="0" width="11" height="9" rx="1" fill="#9b9b9b"/><path d="M0.5 1 5.5 5 10.5 1" stroke="#2e2e2e" fill="none"/></svg>( 0400 ) 118 204</p>
      <p style="margin-top:6px"><svg width="11" height="11" viewBox="0 0 11 11"><path d="M2 0.5 4 3 3 4.5c.7 1.5 2 2.8 3.5 3.5L8 7l2.5 2-1.3 1.5C5 10 1 6 0.5 1.8z" fill="#9b9b9b"/></svg>info@meridale-advisory.com</p>
    </div>
  </div>
</footer>
<div class="footer-base">
  <div class="wrap">
    <span>© 2015. Meridale Growth Advisory. All rights reserved</span>
    <div class="social"><span>Connct with our social network :</span><i></i><i></i><i></i><i></i><i></i></div>
  </div>
</div>

</body>
</html>
```